Billboard design for agricultural machinery business

hello im looking for roadside advertiement sign to be designed, the sign is 10ft up in the air and is 4ft high and 8ft wide, id image i like a blue background and my logo front and centre and below logo sales - service - parts and then below that the brook meadow symbol and tull symbol, I’d also like the website www.Ploverfield.ie on it. i am open to suggestions and designs. blue is #005999 and yellow is rgb (254, 205, 26) ive attached my log and symbols, im open to different colour backgrounds or just white and also open to brook meadow and tull as writhing rather than logos

Target Market(s)

Brook Meadow and tull tractor owners

Industry/Entity Type

Agricultural machine sales service and parts

Colors

Designer to choose colors to be used in the design.

Requirements
Must have
• My logo and colours, brands brook Meadow and tull, website

```html
<!DOCTYPE html>
<html lang="en">
<head>
<meta charset="utf-8">
<title>Ploverfield Roadside Billboard</title>
<link href="https://fonts.googleapis.com/css2?family=Oswald:wght@600&family=Poppins:wght@600;800&display=swap" rel="stylesheet">
<style>
  :root {
    --brand-blue: #145597;
    --brand-yellow: #fecd1a;
    --white: #ffffff;
    --backdrop: #333333;
  }
  * { margin: 0; padding: 0; box-sizing: border-box; }
  html, body {
    width: 1066px;
    height: 1200px;
    overflow: hidden;
    background: var(--backdrop);
  }
  .billboard {
    position: absolute;
    left: 33px;
    top: 350px;
    width: 1000px;
    height: 500px;
    background: var(--brand-blue);
    overflow: hidden;
  }
  .billboard__band {
    position: absolute;
    inset: 0;
    width: 100%;
    height: 100%;
  }
  .brand-logo {
    position: absolute;
    left: 0;
    right: 0;
    top: 140px;
    display: flex;
    justify-content: center;
    align-items: center;
    gap: 18px;
  }
  .brand-logo__name {
    font-family: "Poppins", sans-serif;
    font-weight: 800;
    font-size: 104px;
    line-height: 1;
    color: var(--white);
    letter-spacing: -1px;
  }
  .brand-logo__dot {
    width: 34px;
    height: 34px;
    border-radius: 50%;
    background: var(--brand-yellow);
  }
  .services {
    position: absolute;
    left: 0;
    right: 0;
    top: 352px;
    display: flex;
    justify-content: center;
    align-items: center;
    gap: 14px;
    font-family: "Oswald", sans-serif;
    font-weight: 600;
    font-size: 60px;
    line-height: 1;
    color: var(--brand-blue);
    text-transform: uppercase;
  }
  .services__divider {
    width: 4px;
    height: 56px;
    background: var(--white);
  }
  .partners {
    position: absolute;
    left: 0;
    right: 0;
    top: 432px;
    display: flex;
    justify-content: center;
    align-items: center;
    gap: 26px;
  }
  .partners__brand {
    font-family: "Oswald", sans-serif;
    font-weight: 600;
    font-size: 34px;
    line-height: 1;
    color: var(--brand-blue);
    text-transform: uppercase;
  }
  .partners__website {
    font-family: "Poppins", sans-serif;
    font-weight: 600;
    font-size: 24px;
    line-height: 1;
    color: var(--white);
    background: var(--brand-blue);
    border-radius: 24px;
    padding: 11px 22px;
  }
</style>
</head>
<body>
  <main class="billboard">
    <svg class="billboard__band" viewBox="0 0 1000 500" preserveAspectRatio="none" aria-hidden="true">
      <path d="M0 384 Q470 230 1000 378 L1000 500 L0 500 Z" fill="var(--white)"/>
      <path d="M0 392 Q470 240 1000 388 L1000 500 L0 500 Z" fill="var(--brand-yellow)"/>
    </svg>

    <div class="brand-logo">
      <span class="brand-logo__name">Ploverfield</span>
      <span class="brand-logo__dot"></span>
    </div>

    <div class="services">
      <span class="services__item">Sales</span>
      <span class="services__divider"></span>
      <span class="services__item">Service</span>
      <span class="services__divider"></span>
      <span class="services__item">Parts</span>
    </div>

    <div class="partners">
      <span class="partners__brand">Brook Meadow</span>
      <span class="partners__brand">Tull</span>
      <span class="partners__website">www.Ploverfield.ie</span>
    </div>
  </main>
</body>
</html>
```